VLK IT Solutions Provider

Please read attached documentation completely before beginning Project. Thank you!

Folio Nest Project Requirements

Thank you for your interest in this design contest. We are always welcome to questions and are looking forward to seeing what you can come up with.

The logo is located on the current site homepage http://www.vantolirex.com/

Bootstrap

We work on a Bootstrap platform with our custom built CMS. We require all designs to be

sized accordingly with the bootstrap grid system found here: http://trelvanix.com/css/#grid

Start of Competition Requirements

At the start of a competition, we are looking for general Home Page Design concepts and interior page design concepts as well.

HOME PAGE DESIGN

Any changes requested by the client in the original designs

Responsive Tablet View (using standard bootstrap media queries, we need to see an

example of a tablet size home page view)

Responsive Phone View (using standard bootstrap media queries, we need to see an

example of a phone size home page view)

INTERIOR PAGE DESIGN

These pages are general content pages. Our CMS allows for the creation of unlimited

pages and gives the client control of adding them. Interior Page Designs can be built

with 1 column, 2 columns (either right side bar or left sidebar)

Examples of buttons and button states,

Examples of drop down menus

Examples of H1 through H5 plus body copy

We uploaded a clean logo to use on the project. Thank you.

Project Deadline Extended

We added a updated Creative Brief document to help out. Please take a look thanks!

```html
<!DOCTYPE html>
<html lang="en">
<head>
<meta charset="utf-8">
<title>VLK – Vantolirex Research Group</title>
<link href="https://fonts.googleapis.com/css2?family=Open+Sans:wght@300;400;600;700&display=swap" rel="stylesheet">
<style>
:root{
  --blue:#1f63a9;
  --blue-light:#3a86d2;
  --blue-dark:#17508d;
  --gold-top:#f7c743;
  --gold-bottom:#e7a81c;
  --heading:#1f6db5;
  --text:#444;
  --muted:#7a7a7a;
  --rule:#d8d8d8;
  --footer:#2f2f2f;
  --footer-text:#b8b8b8;
}
*{box-sizing:border-box;margin:0;padding:0}
html,body{width:1104px;height:1200px;overflow:hidden;background:#fff}
body{font-family:"Open Sans",Arial,sans-serif;color:var(--text);position:relative}
.container{position:absolute;left:91px;width:922px}

.site-header{top:0;height:131px}
.brand{position:absolute;left:2px;top:24px;display:flex;align-items:center;gap:10px}
.brand-mark{width:18px;height:18px;border-radius:50%;background:var(--gold-bottom)}
.brand-name{font-size:56px;font-weight:700;color:var(--blue);letter-spacing:2px;line-height:1}
.contact-line{position:absolute;right:0;top:35px;font-size:14px;color:#777;display:flex;align-items:center;gap:8px}
.contact-line a{color:var(--blue);text-decoration:none}
.search{position:absolute;right:0;top:69px;width:182px;height:30px;border:1px solid #ddd;border-radius:2px;display:flex;align-items:center}
.search span{flex:1;font-size:12.5px;color:#999;padding-left:11px}
.search i{width:28px;height:100%;border-left:1px solid #ddd;display:flex;align-items:center;justify-content:center}

.main-nav{top:131px;height:44px;background:linear-gradient(var(--blue-light),var(--blue));display:flex}
.main-nav a{color:#fff;text-decoration:none;font-size:13.5px;height:44px;display:flex;align-items:center;padding:0 20px;border-right:1px solid var(--blue-dark)}
.main-nav a.active{background:linear-gradient(var(--gold-top),var(--gold-bottom));color:#6b4a0a;padding:0 23px}
.nav-social{margin-left:auto;display:flex;gap:16px;align-items:center;padding-right:17px}
.nav-social span{width:30px;height:30px;border-radius:3px;background:linear-gradient(#fff,#dcdcdc)}

.hero{top:180px;height:361px;background:linear-gradient(90deg,#f4f6fa 0%,#eef1f6 40%,#dfe7f0 60%,#c9d7e6 100%)}
.hero-text{position:absolute;left:86px;top:101px;font-size:28.5px;font-weight:300;color:#222;line-height:36.5px}
.hero-btn{position:absolute;left:86px;top:222px;background:linear-gradient(#666,#444);color:#fff;font-size:14px;padding:6px 14px;border-radius:3px}
.hero-arrow{position:absolute;top:168px}

.intro{top:571px;text-align:center;font-size:15.5px;font-weight:300;color:#333;line-height:27px}
.divider{top:682px;height:1px;background:var(--rule)}

.col{position:absolute;top:716px}
.col h2{font-size:23.5px;font-weight:400;color:var(--heading);margin-bottom:7px}
.col p{font-size:12.5px;color:var(--muted);line-height:17.5px;width:292px}
.photo{margin-top:13px;width:288px;height:126px}
.badges{display:flex;gap:22px;margin-top:15px;align-items:center}
.badges span{width:48px;height:48px;background:#d6dbe6;border-radius:50%}
.badges span.sq{border-radius:0;background:#2a4c8c;width:44px}

.news-item{display:flex;gap:13px;margin-bottom:24px}
.news-thumb{width:84px;height:73px;flex:none}
.news-item h3{font-size:12.5px;font-weight:400;color:#222;line-height:15.5px;margin-top:8px}
.news-item time{font-size:12px;color:#999;display:block;margin-top:6px}

.site-footer{position:absolute;left:0;top:1066px;width:1104px;height:134px;background:var(--footer)}
.footer-nav{position:absolute;left:0;width:100%;top:25px;display:flex;justify-content:center;gap:43px;font-size:13px;color:var(--footer-text)}
.footer-rule{position:absolute;left:91px;width:922px;top:64px;height:1px;background:#555}
.copyright{position:absolute;left:93px;top:89px;font-size:13px;color:var(--footer-text)}
.footer-social{position:absolute;right:91px;top:82px;display:flex;gap:10px}
.footer-social span{width:33px;height:33px;border-radius:50%;border:2px solid #1a1a1a}
</style>
</head>
<body>

<header class="container site-header">
  <div class="brand"><span class="brand-mark"></span><span class="brand-name">VLK</span></div>
  <div class="contact-line">
    <svg width="22" height="16" viewBox="0 0 22 16"><path d="M3 2c2-2 4-1 5 1l1 2c0 1-1 2-2 2 1 2 3 4 5 5 0-1 1-2 2-2l2 1c2 1 3 3 1 5-3 2-9-1-12-5S1 4 3 2z" fill="#888"/></svg>
    Call us : <a href="#">(555) 214-7390</a>
  </div>
  <div class="search"><span>Search</span><i><svg width="16" height="16" viewBox="0 0 16 16"><circle cx="6.5" cy="6.5" r="5" fill="none" stroke="#888" stroke-width="2"/><path d="M10 10l5 5" stroke="#888" stroke-width="2.5"/></svg></i></div>
</header>

<nav class="container main-nav">
  <a class="active" href="#">HOME</a>
  <a href="#">ABOUT US</a>
  <a href="#">SERVICES</a>
  <a href="#">PRODUCTS</a>
  <a href="#">DIVISONS</a>
  <a href="#">CAREER</a>
  <a href="#">CONTACT US</a>
  <div class="nav-social"><span></span><span></span><span></span></div>
</nav>

<section class="container hero" role="img" aria-label="Laboratory scientists in white coats, one holding a flask of red liquid">
  <svg class="hero-arrow" style="left:21px" width="18" height="30" viewBox="0 0 18 30"><path d="M15 2L3 15l12 13" fill="none" stroke="#777" stroke-width="2.5"/></svg>
  <div class="hero-text">Technology Solutions for<br>National Defense &amp;<br>Global Security</div>
  <div class="hero-btn">Contact us</div>
  <svg class="hero-arrow" style="right:19px" width="18" height="30" viewBox="0 0 18 30"><path d="M3 2l12 13L3 28" fill="none" stroke="#fff" stroke-width="2.5"/></svg>
</section>

<p class="container intro">Since 1988, Vantolirex Research Group has been providing innovative and cost-effective products and services to customers worldwide. We are a vital source for leading-edge technology solutions that help our customers respond to opportunities faster, achieve more from their operations, and exceed their requirements.</p>

<div class="container divider"></div>

<section class="col" style="left:91px">
  <h2>Our Services</h2>
  <p>Cum sociis natoque penatibus et magnis dis parturient montes, nascetur ridiculus mus. Proin nec posuere lectus. Duis congue tellus purus vulputate, quis volutpat fermentum.</p>
  <div class="photo" role="img" aria-label="Vintage microscope on a wooden desk" style="background:linear-gradient(90deg,#cfcdbb,#b9b39a 60%,#7a6a52)"></div>
  <div class="badges"><span style="background:#fff;border:1.5px solid #5a4fd0"></span><span></span><span class="sq"></span></div>
</section>

<section class="col" style="left:408px">
  <h2>Our Products</h2>
  <p>Cum sociis natoque penatibus et magnis dis parturient montes, nascetur ridiculus mus. Proin nec posuere lectus. Duis congue tellus purus vulputate, quis volutpat fermentum.</p>
  <div class="photo" role="img" aria-label="Glowing digital globe above an open hand" style="background:radial-gradient(circle at 50% 40%,#6cc4ff,#1d5fb4 40%,#0a1f4a 80%)"></div>
</section>

<section class="col" style="left:730px">
  <h2>Latest News</h2>
  <div class="news-item">
    <div class="news-thumb" role="img" aria-label="Seedling in a laboratory dish" style="background:linear-gradient(135deg,#2a6bb0,#dfe8f2 60%,#8ab54a)"></div>
    <div><h3>Quisque auctor metus id arcu auctor, sit amet dapibus sapien accumsan.</h3><time>June 24, 2014</time></div>
  </div>
  <div class="news-item">
    <div class="news-thumb" role="img" aria-label="Researcher examining a DNA model" style="background:linear-gradient(135deg,#3b3f48,#8a8f99 50%,#c9ccd2)"></div>
    <div><h3>Quisque auctor metus id arcu auctor, sit amet dapibus sapien accumsan.</h3><time>June 24, 2014</time></div>
  </div>
  <div class="news-item">
    <div class="news-thumb" role="img" aria-label="Person wearing futuristic visor glasses" style="background:linear-gradient(135deg,#3c3c44,#9a9aa4 50%,#b0343a)"></div>
    <div><h3>Quisque auctor metus id arcu auctor, sit amet dapibus sapien accumsan.</h3><time>June 24, 2014</time></div>
  </div>
</section>

<footer class="site-footer">
  <div class="footer-nav"><span>• Home</span><span>• About us</span><span>• Services</span><span>• Products</span><span>• Divisons</span><span>• Career</span><span>• Contact us</span></div>
  <div class="footer-rule"></div>
  <div class="copyright">Copyright &nbsp;©&nbsp; 2014 &nbsp;Vantolirex Research Group. &nbsp; All rights reserved.</div>
  <div class="footer-social">
    <span style="background:#3b5b9a"></span><span style="background:#2fa9e0"></span><span style="background:#1a84b8"></span><span style="background:#f0772a"></span>
  </div>
</footer>

</body>
</html>
```